Poster for pawn shop lobby

Looking for green and gold as my colors, like the picture shown of my old poster. This time I'm contemplating with doing pictures as well as just text. Here are ideas of things I buy and give loans on. We want to emphasize jewelry, laptops, game systems, tools. I'm open-minded.
Old & Broken Gold
Jewelry & Collectibles
Diamonds
Video Games & Systems
Up-to-date Computers & Laptops
Tablets
Cameras
Power Tools
Home & Garden Equipment
Sports Equipment
Watches
Antique Collectibles
Musical Instruments
And anything else of value
Shop

```html
<!DOCTYPE html>
<html lang="en">
<head>
<meta charset="utf-8">
<title>We Loan or Pay You Cash On – Pawn Shop Poster</title>
<link rel="stylesheet" href="https://fonts.googleapis.com/css2?family=Arimo:wght@400;700&display=swap">
<style>
  :root {
    --green: #00953f;
    --gold: #f2a900;
    --orange: #e8a000;
    --white: #ffffff;
    --faint-dollar: rgba(120, 190, 80, 0.45);
  }
  html, body {
    margin: 0;
    padding: 0;
    overflow: hidden;
    background: #ffffff;
  }
  .poster {
    position: relative;
    width: 850px;
    height: 1200px;
    background: var(--green);
    overflow: hidden;
    font-family: "Arimo", Arial, sans-serif;
    color: var(--white);
  }
  .backdrop {
    position: absolute;
    inset: 0;
    width: 850px;
    height: 1200px;
  }
  .headline {
    margin: 0;
    font-weight: 700;
    font-size: 81px;
    line-height: 81px;
    white-space: nowrap;
  }
  .headline .line {
    position: absolute;
    left: 26px;
  }
  .headline .line-one { top: 64px; }
  .headline .line-two { top: 167px; }
  .headline-dollar {
    position: absolute;
    left: 596px;
    top: 40px;
    font-weight: 400;
    font-size: 118px;
    line-height: 1;
    color: var(--gold);
  }
  .big-dollar {
    position: absolute;
    left: 478px;
    top: 296px;
    font-weight: 400;
    font-size: 560px;
    line-height: 1;
    color: var(--faint-dollar);
  }
  .item-list {
    position: absolute;
    left: 55px;
    top: 400px;
    list-style: none;
    margin: 0;
    padding: 0;
    display: flex;
    flex-direction: column;
    gap: 4px;
  }
  .item {
    height: 48px;
    display: flex;
    align-items: center;
    white-space: nowrap;
    font-size: 28px;
    font-weight: 400;
  }
  .item .bullet {
    width: 34px;
    height: 34px;
    border-radius: 50%;
    background: var(--white);
    margin-right: 18px;
    flex: none;
  }
  .item .dollar {
    color: var(--gold);
    font-size: 44px;
    line-height: 1;
    margin-right: 4px;
  }
  .item--featured {
    font-size: 32px;
    font-weight: 700;
  }
  .item--featured .dollar {
    font-weight: 700;
    font-size: 48px;
  }
  .item--closing {
    font-style: normal;
    color: var(--gold);
    font-weight: 700;
  }
</style>
</head>
<body>
  <main class="poster">
    <svg class="backdrop" viewBox="0 0 850 1200" aria-hidden="true">
      <defs>
        <linearGradient id="cornerGradient" x1="0.3" y1="0.2" x2="1" y2="1">
          <stop offset="0" stop-color="#3f9b34"/>
          <stop offset="0.6" stop-color="#8fa21e"/>
          <stop offset="1" stop-color="#e0a000"/>
        </linearGradient>
      </defs>
      <path d="M850 225 C 830 650, 700 980, 452 1200 L 850 1200 Z" fill="url(#cornerGradient)"/>
      <path d="M0 256 C 260 262, 520 270, 700 262 C 740 258, 768 250, 782 240 C 770 268, 740 284, 690 290 C 480 300, 230 280, 0 262 Z" fill="var(--orange)"/>
    </svg>

    <div class="big-dollar" aria-hidden="true">$</div>

    <h1 class="headline">
      <span class="line line-one">WE LOAN or</span>
      <span class="line line-two">PAY YOU CASH ON</span>
    </h1>
    <div class="headline-dollar" aria-hidden="true">$</div>

    <ul class="item-list">
      <li class="item item--featured"><span class="bullet"></span><span class="dollar">$</span>Old &amp; Broken Gold</li>
      <li class="item item--featured"><span class="bullet"></span><span class="dollar">$</span>Jewelry &amp; Collectibles</li>
      <li class="item"><span class="bullet"></span><span class="dollar">$</span>Diamonds</li>
      <li class="item item--featured"><span class="bullet"></span><span class="dollar">$</span>Video Games &amp; Systems</li>
      <li class="item item--featured"><span class="bullet"></span><span class="dollar">$</span>Up-to-date Computers &amp; Laptops</li>
      <li class="item"><span class="bullet"></span><span class="dollar">$</span>Tablets</li>
      <li class="item"><span class="bullet"></span><span class="dollar">$</span>Cameras</li>
      <li class="item item--featured"><span class="bullet"></span><span class="dollar">$</span>Power Tools</li>
      <li class="item"><span class="bullet"></span><span class="dollar">$</span>Home &amp; Garden Equipment</li>
      <li class="item"><span class="bullet"></span><span class="dollar">$</span>Sports Equipment</li>
      <li class="item"><span class="bullet"></span><span class="dollar">$</span>Watches</li>
      <li class="item"><span class="bullet"></span><span class="dollar">$</span>Antique Collectibles</li>
      <li class="item"><span class="bullet"></span><span class="dollar">$</span>Musical Instruments</li>
      <li class="item item--closing"><span class="bullet"></span><span class="dollar">$</span>And anything else of value</li>
    </ul>
  </main>
</body>
</html>
```